Innovative weight loss company needs reusable bag designs

We are looking to design reusable bags that are COOL. We are an innovative weight loss company that has a focus on versatility, ease, and comfort. We also structure our plan such that clients can travel, eat out, and drink alcohol while losing weight. Because of this, we target to a large number of business men, busy couples, and active moms. We are looking to find a design to use on reusable bags that will look cool, and will inspire the clients to use these bags everyday--for lunches, for traveling, etc. The logo is attached, however, similar to the pinevarra bags that people find cool and use everywhere, there may be a way to portray our ideals and the logo on the bag, while not just placing the logo on the bag. Additionally, I attached the bag shape (but a smaller size). The bag background will most likely be black, navy, or blue.

Target Market(s)

Men and women 40-60

Industry/Entity Type

It Company

Contact Information for Business Card

I would like one side of the business card to be an appointment card, and the other side to have the logo and business details. I am looking for something clean and professional.

Font styles to use
Sans Serif

Requirements
Must have
• The logo or business name. The colors in the logo involved
Should not have
• Any pictures of people eating food, people jumping up and down for health, or other corny, overused weightloss designs.

```html
<!DOCTYPE html>
<html lang="en">
<head>
<meta charset="utf-8">
<title>Drop it Like a Squat — Aveliro tote design</title>
<link rel="stylesheet" href="https://fonts.googleapis.com/css2?family=Lexend+Zetta:wght@100;200&display=swap">
<style>
  :root {
    --bag-black: #000000;
    --ink-white: #ffffff;
    --squat-red: #d7262f;
    --brand-red: #e8203a;
    --brand-blue: #5bc8ee;
  }
  html, body {
    margin: 0;
    padding: 0;
    width: 1200px;
    height: 1200px;
    overflow: hidden;
    background: var(--bag-black);
  }
  .tote-design {
    display: block;
    width: 1200px;
    height: 1200px;
    background: var(--bag-black);
  }
  .slogan {
    font-family: "Lexend Zetta", "Helvetica Neue", Arial, sans-serif;
    font-weight: 100;
    font-size: 156px;
  }
  .slogan-line { fill: var(--ink-white); }
  .slogan-accent { fill: var(--squat-red); }
  .divider { stroke: var(--ink-white); stroke-width: 1.6; }
  .brand-dot { fill: var(--brand-blue); }
  .brand-name {
    font-family: "Lexend Zetta", "Helvetica Neue", Arial, sans-serif;
    font-weight: 200;
    font-size: 44px;
    fill: var(--brand-red);
  }
</style>
</head>
<body>
<svg class="tote-design" viewBox="0 0 1200 1200" xmlns="http://www.w3.org/2000/svg">
  <g class="slogan">
    <text class="slogan-line" x="196" y="346" textLength="816" lengthAdjust="spacingAndGlyphs">Drop it</text>
    <text class="slogan-line" x="232" y="540" textLength="736" lengthAdjust="spacingAndGlyphs">Like a</text>
    <text class="slogan-accent" x="134" y="734" textLength="940" lengthAdjust="spacingAndGlyphs">SQUAT</text>
  </g>

  <line class="divider" x1="142" y1="802" x2="1058" y2="802"/>

  <g class="brand-signoff">
    <circle class="brand-dot" cx="432" cy="976" r="18"/>
    <text class="brand-name" x="470" y="992" textLength="300" lengthAdjust="spacingAndGlyphs">Aveliro</text>
  </g>
</svg>
</body>
</html>
```